Velmora Supply Company product labels (5"wide x7" high (12,5 cm x 17,5 cm))

We need a vertical product label that will go on the Gold stand up bags for our Kratom powder. We are looking for professional looking and attractive label design that will capture the attention of consumers. Our products should stand out when sitting on a shelf next to our competitors. We want one label which we will be able to use for all the different Kratom Powders we have.The product label will be used for several different varieties of Kratom so there will need to be an area available for the varieties name such as "RED BORNEO" or "GREEN MAENG DA" etc., which we will apply a small label as needed.
The label dimensions should be 5" wide x 7" high (12,5 cm wide x 17,5 cm high).
Please review the "must haves" section, and please try and include the "nice to haves" if possible.

Target Market(s)

Health minded consumers who love natural products, and are looking for plant based alternatives to harmful synthetic products.

Industry/Entity Type

Supplement

Colors

Designer to choose colors to be used in the design.

Requirements
Must have
• Product labels must include:
• 1) Company logo (find in the attachments)
• 2) Product information (find in the attachments)
• 3) Product title - Premium Kratom Powder
• 4) Weight indication - 250 grams
• 5) Barcode
• 6) Icon that says - 100% pure (or "100% natural")
Nice to have
• Indonesian jungle theme.
• Our packaging is gold metallic stand up bag, so the colors should be complimenting the bag.
Should not have
• labels or part of the labels taken from other Kratom companies. The design should be unique.

```html
<!DOCTYPE html>
<html lang="en">
<head>
<meta charset="utf-8">
<title>Velmora Supply Company – Premium Powder Label</title>
<link href="https://fonts.googleapis.com/css2?family=Teko:wght@500;600&family=Open+Sans:wght@700;800&family=Alfa+Slab+One&display=swap" rel="stylesheet">
<style>
  :root {
    --backdrop: #262626;
    --label-white: #fbfcf7;
    --leaf-light: #e3edc8;
    --leaf-mid: #c9dc9a;
    --ink-green: #2f4721;
    --badge-green: #4f7d37;
    --badge-text: #eef3e4;
  }
  * { margin: 0; padding: 0; box-sizing: border-box; }
  html, body {
    width: 1200px; height: 1000px; overflow: hidden;
    background: var(--backdrop);
  }
  .label {
    position: absolute; left: 270px; top: 40px;
    width: 660px; height: 920px;
    background: var(--label-white);
    overflow: hidden;
    color: var(--ink-green);
    font-family: "Open Sans", sans-serif;
  }
  .leaf-backdrop {
    position: absolute; inset: 0;
    background:
      radial-gradient(ellipse 60% 45% at 20% 25%, var(--leaf-mid) 0%, transparent 70%),
      radial-gradient(ellipse 55% 40% at 85% 60%, var(--leaf-mid) 0%, transparent 70%),
      radial-gradient(ellipse 50% 35% at 30% 90%, var(--leaf-light) 0%, transparent 75%),
      linear-gradient(160deg, var(--label-white) 0%, var(--leaf-light) 100%);
    opacity: 0.85;
  }
  .brand {
    position: absolute; left: 50%; top: 120px;
    transform: translateX(-50%);
    width: 360px; text-align: center;
  }
  .brand-dot {
    width: 44px; height: 44px; border-radius: 50%;
    background: var(--ink-green);
    margin: 0 auto 14px;
  }
  .brand-name {
    font-family: "Teko", sans-serif; font-weight: 600;
    font-size: 58px; line-height: 0.92; letter-spacing: 2px;
    text-transform: uppercase; color: var(--ink-green);
  }
  .brand-web {
    margin-top: 12px;
    font-size: 12px; font-weight: 700; color: var(--ink-green);
  }
  .product {
    position: absolute; left: 0; right: 0; top: 438px; text-align: center;
  }
  .product-tier {
    font-family: "Teko", sans-serif; font-weight: 500;
    font-size: 38px; letter-spacing: 9px; line-height: 1;
  }
  .product-title {
    font-family: "Teko", sans-serif; font-weight: 600;
    font-size: 84px; line-height: 0.85; letter-spacing: 1px;
  }
  .ingredients {
    position: absolute; left: 90px; right: 30px; top: 586px;
    font-size: 15px; font-weight: 700; letter-spacing: -0.3px;
  }
  .warning {
    position: absolute; left: 60px; right: 60px; top: 620px;
    text-align: center; font-size: 15px; font-weight: 800;
    line-height: 1.3; text-transform: uppercase; letter-spacing: -0.2px;
  }
  .natural-badge {
    position: absolute; left: 146px; top: 712px;
    width: 228px; height: 136px;
    background: var(--badge-green);
    border-radius: 8px;
    display: flex; flex-direction: column; align-items: center; justify-content: center;
    outline: 4px solid var(--badge-green); outline-offset: 5px;
  }
  .natural-badge span {
    font-family: "Alfa Slab One", serif; color: var(--badge-text);
    line-height: 1.05; letter-spacing: 2px;
  }
  .natural-badge .pct { font-size: 44px; }
  .natural-badge .word { font-size: 31px; }
  .net-weight {
    position: absolute; left: 455px; top: 738px; width: 90px;
    text-align: center;
    font-family: "Teko", sans-serif; font-weight: 600;
    font-size: 44px; line-height: 0.85;
  }
  .distributor {
    position: absolute; left: 0; right: 0; top: 880px;
    text-align: center; font-size: 12px; font-weight: 700;
  }
</style>
</head>
<body>
  <main class="label">
    <div class="leaf-backdrop" role="img" aria-label="Soft pattern of pale green jungle leaves with fine veins"></div>

    <header class="brand">
      <div class="brand-dot"></div>
      <div class="brand-name">Velmora<br>Supply Company</div>
      <div class="brand-web">www.velmorasupply.com</div>
    </header>

    <section class="product">
      <div class="product-tier">PREMIUM</div>
      <h1 class="product-title">KRATOM POWDER</h1>
    </section>

    <p class="ingredients">Ingredients: 100% natural Mitragyna Speciosa leaf powder.</p>
    <p class="warning">Not for sale to minors. Must be 18 years<br>or older to purchase. Keep out of reach of<br>children</p>

    <div class="natural-badge">
      <span class="pct">100%</span>
      <span class="word">NATURAL</span>
    </div>

    <div class="net-weight">250<br>GR</div>

    <p class="distributor">Distributed by: VELMORA SUPPLY COMPANY PINECREST, FL 32999</p>
  </main>
</body>
</html>
```